Business Card/ Banner/ Logo/ Shirt design for (Meadowlark total Health Club) already have a rough idea

Hi,

I designed the business Meadowlark Total Health Club to create an environment where people could walk in to and feel at home, a place they could love and talk to all their friends about. I run group classes, personal training and gym activities however my interaction with clients is on a much deeper level and I help them with inspiration and life coaching improving their life with a holistic approach. I want meadowlark to become global and be seen as the benchmark for professionalism, yet compassion, wellness and an ora of unconditional love and care for its clients and members. I created Meadowlark so that people could experience life, energy and passion and begin to really love, enjoy, thrive, create and embrace their dreams and follow them.

I have made a logo that I feel best captures this mission however I used it using Microsoft word and paint so in terms of using it as a template the resolution could become distorted.

So I really reach out to the designers that want to be part of something passionate and help the meadowlark logo, design and vision come to physical form.

I like the logo I have created and I like purple as a feature colour, however I am open to any alterations or tweaks that your designer prowess may feel that will fit with the mission, description and vision the Meadowlark Total Health Club will carry of to invigorate the lives of millions.

I am also looking for a shirt design that looks professional and modern as well as fresh with life and credibility

I appreciate your time, thank you and I would love to have your inspired ideas come to life :)

Regards Tom

If you need to contact me

Email tomberrington@fernmail.net
Mob 0473 219 604

Industry/Entity Type

Life Coaching

Contact Information for Business Card

Meadowlark Total Health Club, fitness studio and wellness centre

Logo styles of interest
Emblem Logo
Pictorial/Combination Logo
Abstract Logo
Character Logo
Wordmark Logo
Lettermark Logo
Requirements
Nice to have
• Purple, original "M" logo
Tag line "the essence of energy"

```html
<!DOCTYPE html>
<html lang="en">
<head>
<meta charset="utf-8">
<title>Meadowlark Total Health Club – Business Card</title>
<link rel="stylesheet" href="https://fonts.googleapis.com/css2?family=Open+Sans:wght@400;600&display=swap">
<style>
  :root {
    --backdrop: #2b2b2d;
    --purple-deep: #2e1150;
    --purple: #3d1a68;
    --purple-mid: #5b2f8f;
    --purple-soft: #8a64bd;
    --lilac: #b9a3d9;
    --paper: #ffffff;
    --paper-shade: #dcdce0;
    --ink: #2f1454;
  }
  * { box-sizing: border-box; margin: 0; padding: 0; }
  html, body {
    width: 1200px; height: 900px; overflow: hidden;
    background: var(--backdrop);
    font-family: "Open Sans", Arial, sans-serif;
  }
  .canvas { position: relative; width: 1200px; height: 900px; }

  .card {
    position: absolute; left: 320px; width: 560px; height: 320px;
    border-radius: 26px; overflow: hidden;
  }

  /* Front */
  .card--front {
    top: 90px;
    background: linear-gradient(160deg, var(--purple) 0%, var(--purple-deep) 100%);
    color: var(--paper);
  }
  .brand { position: absolute; display: flex; align-items: center; gap: 12px; }
  .brand__mark { width: 22px; height: 22px; flex: none; }
  .brand__name { font-weight: 600; font-size: 26px; letter-spacing: 0.2px; white-space: nowrap; }
  .tagline {
    position: absolute; font-size: 12px; letter-spacing: 4px; text-transform: uppercase; white-space: nowrap;
  }
  .card--front .brand { left: 80px; top: 118px; }
  .card--front .brand__mark { background: var(--lilac); }
  .card--front .tagline { left: 114px; top: 160px; color: var(--lilac); }
  .card--front .motto {
    position: absolute; left: 0; right: 0; bottom: 24px; text-align: center;
    font-size: 11px; color: var(--purple-soft); letter-spacing: 0.3px;
  }

  /* Back */
  .card--back {
    top: 490px;
    background: linear-gradient(150deg, var(--paper) 40%, var(--paper-shade) 100%);
    color: var(--ink);
  }
  .card__band { position: absolute; inset: 0; width: 560px; height: 320px; }
  .card--back .brand { left: 34px; top: 174px; gap: 10px; }
  .card--back .brand__mark { width: 20px; height: 20px; background: var(--purple-mid); }
  .card--back .brand__name { font-size: 20px; color: var(--ink); }
  .card--back .tagline { left: 64px; top: 204px; font-size: 9.5px; letter-spacing: 3.2px; color: var(--purple-mid); }

  .contact { position: absolute; left: 290px; top: 32px; }
  .contact__name { font-size: 19px; font-weight: 400; }
  .contact__role { font-size: 11px; margin-top: 2px; }
  .contact__list { list-style: none; margin-top: 14px; font-size: 11px; }
  .contact__list li { display: flex; align-items: center; gap: 9px; margin-bottom: 6px; white-space: nowrap; }
  .contact__list svg { width: 13px; height: 13px; flex: none; }

  .services {
    position: absolute; left: 0; right: 0; bottom: 16px; text-align: center;
    color: var(--lilac); font-size: 14px; letter-spacing: 0.6px; text-transform: uppercase;
  }
</style>
</head>
<body>
<main class="canvas">

  <section class="card card--front" aria-label="Card front">
    <div class="brand">
      <span class="brand__mark"></span>
      <span class="brand__name">meadowlark total health club</span>
    </div>
    <p class="tagline">The essence of energy</p>
    <p class="motto">Improve every area of your life • Make the meadowlark • Find your missing spark</p>
  </section>

  <section class="card card--back" aria-label="Card back">
    <svg class="card__band" viewBox="0 0 560 320" aria-hidden="true">
      <path d="M0 278 C 200 268, 400 240, 560 180 L560 320 L0 320 Z" fill="var(--purple)"/>
      <path d="M0 250 C 150 244, 300 232, 420 208 C 300 238, 150 256, 0 266 Z" fill="var(--purple-soft)"/>
      <path d="M0 278 C 200 268, 400 240, 560 180 L560 189 C 400 248, 200 276, 0 286 Z" fill="var(--purple-deep)" opacity="0.5"/>
    </svg>

    <div class="contact">
      <h1 class="contact__name">Tom Berrington</h1>
      <p class="contact__role">Head coach, Trainer and Owner</p>
      <ul class="contact__list">
        <li>
          <svg viewBox="0 0 12 12"><rect x="3" y="0.5" width="6" height="11" rx="1" fill="none" stroke="var(--purple-mid)" stroke-width="1.2"/><circle cx="6" cy="9.6" r="0.7" fill="var(--purple-mid)"/></svg>
          0473 219 604
        </li>
        <li>
          <svg viewBox="0 0 12 12"><rect x="0.5" y="2.5" width="11" height="7" fill="var(--purple-mid)"/><path d="M0.5 2.5 L6 6.5 L11.5 2.5" fill="none" stroke="var(--paper)" stroke-width="1"/></svg>
          tomberrington@fernmail.net
        </li>
        <li>
          <svg viewBox="0 0 12 12"><circle cx="6" cy="6" r="5.3" fill="var(--purple-mid)"/><path d="M0.8 6 H11.2 M6 0.8 C3.5 3.5 3.5 8.5 6 11.2 M6 0.8 C8.5 3.5 8.5 8.5 6 11.2" fill="none" stroke="var(--paper)" stroke-width="0.7"/></svg>
          www.meadowlarktotalhealth.com.au
        </li>
      </ul>
    </div>

    <div class="brand">
      <span class="brand__mark"></span>
      <span class="brand__name">meadowlark total health club</span>
    </div>
    <p class="tagline">The essence of energy</p>

    <p class="services">Fitness studio and wellness centre</p>
  </section>

</main>
</body>
</html>
```